Brisk Mend - Handyman and Home Repair Services

I need a business card/letterhead logo for my new handyman service in my local area. I'm happy for a logo design to be done prior to business card design so it can be incorporated on to the card, for which I'd be happy to pay more for. I'd like it to be modern and not using the typical pictures of tools and cartoon characters in dungarees! I like the idea of tools but in a more modern way i.e subtle background images in different shades to main colour. I do like the american retro designs and those that show age and patina for example, having an image half old, half new in its appearance to represent the repairing of things. Colours in mind are 1950's retro colours, ie using grey with pastel greens, red and cream. I'd like to break the mould and the stigma thats attached to these jobs and make it more cool and up to date. I hope this will attract interior designers and more modern businesses to use my services.

This is the logo design I like and would be happy for this idea and colours:

http://pavo-sunlark.co.uk/wp-content/uploads/2011/01/p-s_logo600px.png

Industry/Entity Type

Handyman

```html
<!DOCTYPE html>
<html lang="en">
<head>
<meta charset="utf-8">
<title>Brisk Mend – Business Card</title>
<link href="https://fonts.googleapis.com/css2?family=Arvo:wght@400;700&family=Questrial&display=swap" rel="stylesheet">
<style>
  :root {
    --backdrop: #e6e4df;
    --card-top: #fbf7ec;
    --card-fade: #ece5d2;
    --retro-red: #c4463b;
    --mint-light: #9fcfb4;
    --mint-deep: #5f9c80;
    --swoosh: #8f9397;
    --ink-charcoal: #3b4246;
    --ink-grey: #6b6f72;
    --ink-white: #ffffff;
  }
  html, body {
    margin: 0;
    width: 1200px;
    height: 899px;
    overflow: hidden;
    background: var(--backdrop);
  }
  .business-card {
    position: absolute;
    left: 170px;
    top: 200px;
    width: 860px;
    height: 500px;
    border-radius: 44px;
    overflow: hidden;
    background: linear-gradient(180deg, var(--card-top) 0%, var(--card-fade) 70%);
    box-shadow: 0 10px 30px rgba(0,0,0,0.18);
  }
  .card-shapes {
    position: absolute;
    inset: 0;
  }
  .brand {
    position: absolute;
    left: 70px;
    top: 56px;
    display: flex;
    align-items: center;
    gap: 22px;
  }
  .brand-mark {
    width: 86px;
    height: 86px;
    background: var(--mint-deep);
  }
  .brand-name {
    font-family: "Arvo", serif;
    font-weight: 700;
    font-size: 64px;
    line-height: 1;
    color: var(--retro-red);
    margin: 0;
  }
  .brand-tagline {
    font-family: "Arvo", serif;
    font-weight: 400;
    font-size: 18px;
    color: var(--ink-grey);
    margin: 6px 0 0 4px;
  }
  .holder {
    position: absolute;
    left: 150px;
    top: 186px;
    font-family: "Questrial", sans-serif;
  }
  .holder-name {
    font-size: 30px;
    line-height: 36px;
    letter-spacing: 1px;
    color: var(--ink-charcoal);
    margin: 0;
  }
  .holder-role {
    font-size: 20px;
    line-height: 24px;
    letter-spacing: 1px;
    color: var(--retro-red);
    margin: 2px 0 0 0;
  }
  .contact {
    position: absolute;
    right: 44px;
    top: 262px;
    text-align: right;
    font-family: "Questrial", sans-serif;
    color: var(--ink-white);
    margin: 0;
    padding: 0;
    list-style: none;
  }
  .contact-address {
    font-size: 19px;
    line-height: 1.3;
    margin-bottom: 12px;
  }
  .contact-line {
    display: flex;
    justify-content: flex-end;
    align-items: center;
    gap: 12px;
    font-size: 17px;
    height: 29px;
  }
  .contact-icon {
    width: 18px;
    height: 18px;
    fill: var(--ink-white);
  }
</style>
</head>
<body>
  <div class="business-card">
    <svg class="card-shapes" viewBox="0 0 860 500" width="860" height="500" aria-hidden="true">
      <defs>
        <linearGradient id="bandGradient" x1="0" y1="0" x2="1" y2="1">
          <stop offset="0" stop-color="#9fcfb4"/>
          <stop offset="1" stop-color="#5f9c80"/>
        </linearGradient>
      </defs>
      <path d="M0,340 C280,350 580,280 860,92 L860,500 L0,500 Z" fill="url(#bandGradient)"/>
      <path d="M40,318 C320,310 610,240 860,60 C640,238 360,322 40,318 Z" fill="var(--swoosh)"/>
    </svg>

    <div class="brand">
      <div class="brand-mark"></div>
      <div>
        <h1 class="brand-name">Brisk Mend</h1>
        <p class="brand-tagline">Handyman and Home Repair Services</p>
      </div>
    </div>

    <div class="holder">
      <p class="holder-name">OWEN ASHCOMBE</p>
      <p class="holder-role">LEAD HANDYMAN</p>
    </div>

    <ul class="contact">
      <li class="contact-address">214 Harrow Lane Unit 6<br>Kelby KB4</li>
      <li class="contact-line">014 262 7730
        <svg class="contact-icon" viewBox="0 0 24 24"><path d="M6.6 10.8a15 15 0 0 0 6.6 6.6l2.2-2.2a1 1 0 0 1 1-.25 11.4 11.4 0 0 0 3.6.57 1 1 0 0 1 1 1V20a1 1 0 0 1-1 1A17 17 0 0 1 3 4a1 1 0 0 1 1-1h3.5a1 1 0 0 1 1 1c0 1.25.2 2.450.57 3.57a1 1 0 0 1-.25 1Z"/></svg>
      </li>
      <li class="contact-line">014 262 7731
        <svg class="contact-icon" viewBox="0 0 24 24"><path d="M7 1h10a2 2 0 0 1 2 2v18a2 2 0 0 1-2 2H7a2 2 0 0 1-2-2V3a2 2 0 0 1 2-2Zm0 3v14h10V4Zm5 15.5a1 1 0 1 0 0 2 1 1 0 0 0 0-2Z"/></svg>
      </li>
      <li class="contact-line">014 262 7732
        <svg class="contact-icon" viewBox="0 0 24 24"><path d="M6 2h10l2 2v5H6Zm-2 8h16a2 2 0 0 1 2 2v6h-4v4H6v-4H2v-6a2 2 0 0 1 2-2Zm4 7v3h8v-3Z"/></svg>
      </li>
      <li class="contact-line">hi@briskmend.co
        <svg class="contact-icon" viewBox="0 0 24 24"><path d="M2 5h20v14H2Zm2 2v.5l8 5 8-5V7Zm0 2.9V17h16V9.9l-8 5Z"/></svg>
      </li>
      <li class="contact-line">www.briskmendhome.co
        <svg class="contact-icon" viewBox="0 0 24 24"><path d="M12 2a10 10 0 1 0 0 20 10 10 0 0 0 0-20Zm6.9 6h-3a15 15 0 0 0-1.3-3.9A8 8 0 0 1 18.9 8ZM12 4c.9 1.2 1.6 2.5 2 4h-4c.4-1.5 1.1-2.8 2-4ZM4.3 14a8 8 0 0 1 0-4h3.4a16 16 0 0 0 0 4Zm.8 2h3a15 15 0 0 0 1.3 3.9A8 8 0 0 1 5.1 16Zm3-8h-3a8 8 0 0 1 4.3-3.9A15 15 0 0 0 8.1 8ZM12 20c-.9-1.2-1.6-2.5-2-4h4c-.4 1.5-1.1 2.8-2 4Zm2.3-6H9.7a14 14 0 0 1 0-4h4.6a14 14 0 0 1 0 4Zm.3 5.9a15 15 0 0 0 1.3-3.9h3a8 8 0 0 1-4.3 3.9Zm1.7-5.9a16 16 0 0 0 0-4h3.4a8 8 0 0 1 0 4Z"/></svg>
      </li>
    </ul>
  </div>
</body>
</html>
```